Varnel Solutions requires a new business card.

We are an online professional tool store.

Target Market(s)

We target the professional technician.

Industry/Entity Type

Business

Contact Information for Business Card

VarnelSolutions.com.au

sales@varnelsolutions.com

Requirements
Must have
• Needs to look commercial and professional
Should not have
• No Australian Colors, maps or shapes.
• No Shapes of Tools

```html
<!DOCTYPE html>
<html lang="en">
<head>
<meta charset="utf-8">
<title>Varnel Solutions — Business Card</title>
<link href="https://fonts.googleapis.com/css2?family=Poppins:wght@400;500;600&display=swap" rel="stylesheet">
<style>
  :root {
    --page-bg: #e9eaec;
    --card-dark: #161618;
    --card-dark-edge: #232326;
    --card-light: #ffffff;
    --brand-blue: #2f45a8;
    --accent-blue: #1f8fcf;
    --ink: #3d3d42;
    --ink-light: #f2f2f2;
  }
  * { box-sizing: border-box; margin: 0; padding: 0; }
  html, body {
    width: 1200px;
    height: 930px;
    overflow: hidden;
    background: var(--page-bg);
    font-family: "Poppins", sans-serif;
  }
  .card {
    position: absolute;
    width: 560px;
    height: 320px;
    border-radius: 18px;
    box-shadow: 0 10px 30px rgba(0,0,0,0.18);
  }
  .card-back {
    left: 90px;
    top: 110px;
    background: linear-gradient(160deg, var(--card-dark-edge), var(--card-dark));
  }
  .card-front {
    left: 550px;
    top: 500px;
    background: var(--card-light);
  }
  .brand {
    display: flex;
    align-items: center;
    gap: 14px;
    font-weight: 600;
    color: var(--brand-blue);
    white-space: nowrap;
  }
  .brand-dot {
    border-radius: 50%;
    background: var(--brand-blue);
    flex: none;
  }
  .card-back .brand {
    position: absolute;
    left: 50%;
    top: 118px;
    transform: translateX(-50%);
    font-size: 40px;
  }
  .card-back .brand-dot { width: 38px; height: 38px; }
  .back-url {
    position: absolute;
    left: 0;
    right: 0;
    bottom: 40px;
    text-align: center;
    font-size: 15px;
    color: var(--ink-light);
    letter-spacing: 0.3px;
  }
  .back-url .url-name { color: var(--accent-blue); }
  .card-front .brand {
    position: absolute;
    left: 34px;
    top: 140px;
    font-size: 27px;
  }
  .card-front .brand-dot { width: 26px; height: 26px; }
  .divider {
    position: absolute;
    left: 300px;
    top: 70px;
    width: 2px;
    height: 180px;
    background: var(--accent-blue);
  }
  .contact {
    position: absolute;
    left: 320px;
    top: 62px;
    color: var(--ink);
  }
  .contact-name {
    font-size: 21px;
    font-weight: 500;
    color: var(--accent-blue);
    letter-spacing: 0.5px;
    line-height: 1.1;
  }
  .contact-role {
    font-size: 12px;
    letter-spacing: 0.5px;
    margin-bottom: 12px;
  }
  .contact-address {
    font-size: 12.5px;
    line-height: 1.35;
    margin-bottom: 10px;
  }
  .contact-list { list-style: none; font-size: 12.5px; line-height: 1.55; }
  .contact-list li { display: flex; align-items: center; gap: 8px; }
  .contact-list svg { width: 11px; height: 11px; fill: var(--accent-blue); flex: none; }
</style>
</head>
<body>
  <section class="card card-back" aria-label="Card back">
    <div class="brand"><span class="brand-dot"></span>Varnel Solutions</div>
    <p class="back-url">www.<span class="url-name">VarnelSolutions</span>.com.au</p>
  </section>

  <section class="card card-front" aria-label="Card front">
    <div class="brand"><span class="brand-dot"></span>Varnel Solutions</div>
    <div class="divider"></div>
    <div class="contact">
      <p class="contact-name">DARREN KOVIC</p>
      <p class="contact-role">FOUNDER</p>
      <p class="contact-address">14 Alder Court,<br>Fairview TX 75069</p>
      <ul class="contact-list">
        <li><svg viewBox="0 0 24 24"><path d="M6.6 10.8a15 15 0 0 0 6.6 6.6l2.2-2.2c.3-.3.7-.4 1-.2 1.1.4 2.3.6 3.6.6.6 0 1 .4 1 1V20c0 .6-.4 1-1 1C10.6 21 3 13.4 3 4c0-.6.4-1 1-1h3.5c.6 0 1 .4 1 1 0 1.3.2 2.5.6 3.6.1.3 0 .7-.2 1z"/></svg>(555) 014-2873</li>
        <li><svg viewBox="0 0 24 24"><path d="M7 1h10a2 2 0 0 1 2 2v18a2 2 0 0 1-2 2H7a2 2 0 0 1-2-2V3a2 2 0 0 1 2-2zm0 3v15h10V4zm5 16.2a1 1 0 1 0 0 .1z"/></svg>(555) 014-2873</li>
        <li><svg viewBox="0 0 24 24"><path d="M2 5h20v14H2zm2 2v.5l8 5 8-5V7z"/></svg>sales@varnelsolutions.com</li>
        <li><svg viewBox="0 0 24 24"><path d="M12 2a10 10 0 1 0 0 20 10 10 0 0 0 0-20zm6.9 6h-3a15 15 0 0 0-1.4-4A8 8 0 0 1 18.9 8zM12 4c.8 1.2 1.5 2.5 1.9 4h-3.8c.4-1.5 1.1-2.8 1.9-4zM4.3 14a8 8 0 0 1 0-4h3.4a16 16 0 0 0 0 4zm.8 2h3a15 15 0 0 0 1.4 4A8 8 0 0 1 5.1 16zm3-8h-3a8 8 0 0 1 4.4-4 15 15 0 0 0-1.4 4zM12 20c-.8-1.2-1.5-2.5-1.9-4h3.8c-.4 1.5-1.1 2.8-1.9 4zm2.3-6H9.7a14 14 0 0 1 0-4h4.6a14 14 0 0 1 0 4zm.2 6a15 15 0 0 0 1.4-4h3a8 8 0 0 1-4.4 4zm1.8-6a16 16 0 0 0 0-4h3.4a8 8 0 0 1 0 4z"/></svg>VarnelSolutions.com.au</li>
      </ul>
    </div>
  </section>
</body>
</html>
```